Re-design / re-work of existing website

Need to re-design a website so it's easy for me as a user to update/add pictures and change descriptions.

If possible, would there be a way to display LodgeVista calendars? We have 3 cottages and it would be ideal to have each cottage with pics on one page along with a readonly version of the LodgeVista calendar plugin (if such a thing exists) so that visitors to the site can see what is available and what is not.

Existing site: http://tarnwoodlets.net

```html
<!DOCTYPE html>
<html lang="en">
<head>
<meta charset="utf-8">
<title>Tarnwood Bay Cottages</title>
<link href="https://fonts.googleapis.com/css2?family=Playfair+Display:wght@600;700&family=Poppins:wght@400;500;600&display=swap" rel="stylesheet">
<style>
:root{
  --ink:#1d1d1d;
  --text:#3a3a3a;
  --muted:#f5f5f5;
  --white:#ffffff;
  --black:#0d0d0d;
  --accent:#4a4a4a;
  --map:#dedede;
}
*{box-sizing:border-box;margin:0;padding:0}
html,body{width:1200px;height:4240px;overflow:hidden}
body{position:relative;background:var(--white);font-family:"Poppins",sans-serif;color:var(--text)}
.serif{font-family:"Playfair Display",serif;font-weight:700;color:var(--ink)}

/* hero */
.hero{position:absolute;left:0;top:0;width:1200px;height:620px;
  background:linear-gradient(180deg,#6c7f95 0%,#8c9db0 28%,#5b6f86 45%,#7a6a45 62%,#4d5a2e 80%,#3c4526 100%)}
.hero-overlay{position:absolute;inset:0;background:linear-gradient(90deg,rgba(20,25,30,.25),rgba(0,0,0,0) 50%,rgba(210,150,60,.35))}
.brand{position:absolute;left:112px;top:74px;color:var(--white);font-size:17px;font-weight:500;display:flex;align-items:center;gap:8px;white-space:nowrap}
.brand .mark{width:12px;height:12px;border:2px solid var(--white)}
.topbar{position:absolute;top:22px;left:568px;display:flex;align-items:center;gap:20px;color:var(--white);font-size:14.5px}
.pill{border:2px solid var(--white);border-radius:22px;padding:5px 20px;color:var(--white);font-size:14.5px;font-weight:500;display:flex;align-items:center;gap:6px}
.nav{position:absolute;top:78px;left:370px;display:flex;gap:39px;color:var(--white);font-size:15.5px;white-space:nowrap}
.hero-title{position:absolute;top:218px;width:1200px;text-align:center;color:var(--white);font-size:42px}
.btn-outline{position:absolute;border:3px solid var(--white);border-radius:30px;background:rgba(30,30,30,.55);color:var(--white);display:flex;align-items:center;justify-content:center}

/* cottages */
.cottages{position:absolute;left:0;top:620px;width:1200px;height:549px;background:var(--muted)}
.h2{position:absolute;width:1200px;text-align:center;font-size:42px}
.cottage-img{position:absolute;top:785px;width:293px;height:212px;border-radius:8px}
.cottage-card{position:absolute;top:960px;width:262px;height:110px;background:var(--white);border-radius:8px;box-shadow:0 4px 16px rgba(0,0,0,.06);text-align:center}
.cottage-card h3{font-family:"Playfair Display",serif;font-weight:600;font-size:21px;color:var(--ink);margin-top:20px}
.cottage-card a{display:inline-block;margin-top:10px;font-size:15px;font-weight:500;color:var(--ink);text-decoration:none;border-bottom:1px solid var(--ink)}

/* about */
.ring{position:absolute;left:91px;top:1268px;width:434px;height:434px;border:3px solid var(--black);border-radius:50%}
.ring-photo{position:absolute;left:104px;top:1281px;width:408px;height:408px;border-radius:50%;
  background:linear-gradient(180deg,#2b3a34 0%,#2f4a3f 45%,#6a6058 55%,#2a4048 70%,#1a2b31 100%)}
.about-title{position:absolute;left:548px;top:1268px;font-size:40px;line-height:49px}
.about-text{position:absolute;left:548px;top:1391px;width:550px;font-size:15.5px;line-height:24px;color:var(--text)}

/* booking */
.booking{position:absolute;left:0;top:1840px;width:1200px;height:770px;
  background:linear-gradient(180deg,#3d4656 0%,#5a5566 35%,#6e5a5e 55%,#4a3e42 75%,#2c2528 100%)}
.calendar{position:absolute;left:130px;top:2082px;width:438px;height:326px;background:var(--white)}
.cal-tab{position:absolute;top:6px;font-size:12px;color:var(--ink);border:1px solid #ddd;border-radius:3px;padding:2px 8px}
.cal-title{position:absolute;top:40px;width:438px;text-align:center;font-size:18px;font-weight:600;color:var(--ink)}
.cal-cell{position:absolute;width:24px;margin-left:-12px;text-align:center;font-size:11px;color:var(--text);line-height:24px}
.cal-head{font-weight:500;color:var(--ink)}
.cal-today{background:var(--accent);color:var(--white);border-radius:50%}
.event-img{position:absolute;left:591px;width:137px;height:96px;border:3px solid var(--white)}
.event{position:absolute;left:749px;width:320px;color:var(--white)}
.event .date{font-size:15px;font-weight:600;display:flex;align-items:center;gap:5px}
.event .title{font-size:18px;font-weight:600;margin-top:4px}
.event .desc{font-size:12.5px;line-height:17px;margin-top:4px}

/* explore */
.tile{position:absolute;width:293px;height:236px;border-radius:8px;overflow:hidden}
.tile::after{content:"";position:absolute;inset:0;background:linear-gradient(180deg,rgba(0,0,0,0) 45%,rgba(0,0,0,.45))}
.tile span{position:absolute;left:0;right:0;bottom:22px;text-align:center;color:var(--white);font-size:21px;font-weight:500;line-height:26px;z-index:1}

/* map */
.map{position:absolute;left:0;top:3449px;width:1200px;height:383px;background:var(--map)}
.map-pin{position:absolute;left:529px;top:3610px;width:72px;height:72px;border-radius:50%;background:var(--black)}

/* footer */
.footer{position:absolute;left:0;top:3832px;width:1200px;height:408px;background:var(--black);color:var(--white)}
.footer-brand{position:absolute;left:477px;top:36px;width:246px;height:137px;background:#1b1b1b;display:flex;align-items:center;justify-content:center;font-size:18px;font-weight:500;color:var(--white)}
.contact{position:absolute;top:198px;display:flex;align-items:center;gap:16px;font-size:15.5px;line-height:23px}
.icon-ring{width:50px;height:50px;border:2px solid var(--white);border-radius:50%;display:flex;align-items:center;justify-content:center}
.footer-nav{position:absolute;top:290px;left:0;width:1200px;display:flex;justify-content:center;gap:40px;font-size:16px}
.copyright{position:absolute;top:346px;width:1200px;text-align:center;font-size:15px}
</style>
</head>
<body>

<header class="hero" role="img" aria-label="Red cottage on a hillside above a lake with mountains and wildflowers">
  <div class="hero-overlay"></div>
  <div class="brand"><span class="mark"></span>Tarnwood Bay Cottages</div>
  <div class="topbar">
    <span style="display:flex;align-items:center;gap:6px">
      <svg width="13" height="13" viewBox="0 0 24 24" fill="#fff"><path d="M6.6 10.8a15.1 15.1 0 0 0 6.6 6.6l2.2-2.2c.3-.3.7-.4 1-.2 1.1.4 2.3.6 3.6.6.6 0 1 .4 1 1V20c0 .6-.4 1-1 1C10.6 21 3 13.4 3 4c0-.6.4-1 1-1h3.5c.6 0 1 .4 1 1 0 1.3.2 2.5.6 3.6.1.3 0 .7-.2 1z"/></svg>
      Call Us +1 555 014 2290</span>
    <span class="pill"><svg width="12" height="12" viewBox="0 0 24 24" fill="#fff"><rect x="3" y="5" width="18" height="16" rx="2"/></svg>Book Now</span>
    <span class="pill">Getting Here</span>
  </div>
  <nav class="nav"><span>Home</span><span>Our Cottages</span><span>Adventures</span><span>Contact Us</span><span>Today's Weather</span><span>Policies</span></nav>
  <h1 class="hero-title serif" style="color:#fff">Tarnwood Bay Cottages!</h1>
  <div class="btn-outline" style="left:514px;top:296px;width:172px;height:56px;font-family:'Playfair Display',serif;font-size:21px;font-weight:600">Book Now</div>
</header>

<section class="cottages"></section>
<h2 class="h2 serif" style="top:700px">Our Cottages</h2>
<div class="cottage-img" role="img" aria-label="Aspen cottage bedroom" style="left:128px;background:linear-gradient(135deg,#6f7a74,#a89a88 60%,#5a3f30)"></div>
<div class="cottage-img" role="img" aria-label="Birch cottage living room with wood panelling" style="left:453px;background:linear-gradient(135deg,#b0896a,#7a4e33 60%,#d8d2c8)"></div>
<div class="cottage-img" role="img" aria-label="Cedar cottage living room with lake view" style="left:778px;background:linear-gradient(135deg,#7d8a84,#c9d3d8 55%,#6a4a38)"></div>
<div class="cottage-card" style="left:145px"><h3>The Aspen</h3><a>View Calendar &rsaquo;</a></div>
<div class="cottage-card" style="left:470px"><h3>The Birch</h3><a>View Calendar &rsaquo;</a></div>
<div class="cottage-card" style="left:795px"><h3>The Cedar</h3><a>View Calendar &rsaquo;</a></div>

<div class="ring"></div>
<div class="ring-photo" role="img" aria-label="Lit cabin among pine trees reflected in a calm lake"></div>
<h2 class="about-title serif">Killarney/ French River,<br>Ontario, Canada</h2>
<p class="about-text">Come and enjoy life on the water! This south facing property promises long sun filled days and a gorgeous sunrise, along with unlimited family fun and relaxation.&nbsp; The location is perfect, and guests will undoubtedly enjoy everything this Killarney /French River destination has to offer. The rock outcroppings and majestic topography along the pristine waters is a sight to behold.&nbsp; Make Tarnwood Bay cottages your hub to visit the various brag worthy destinations, such as The Killarney, French River and Grundy Lake provincial parks, or just relax and kick back at the cottages, that have it all. For a quaint town experience, and last-minute shopping, drive down via a scenic drive to the towns of Alban, Noellville or Monetville. A week is merely an ice breaker for everything this place has to offer!</p>

<section class="booking" role="img" aria-label="Lake at dusk with a wooden dock and forested shoreline"></section>
<h2 class="h2 serif" style="top:1972px;color:#fff">Booking Calendars</h2>

<div class="calendar">
  <span class="cal-tab" style="left:6px">&lsaquo; May 2023</span>
  <span class="cal-tab" style="right:6px">July 2023 &rsaquo;</span>
  <div class="cal-title">&#9638; June 2023</div>
  <span class="cal-cell cal-head" style="left:43px;top:92px">SUN</span>
  <span class="cal-cell cal-head" style="left:100px;top:92px">MON</span>
  <span class="cal-cell cal-head" style="left:156px;top:92px">TUE</span>
  <span class="cal-cell cal-head" style="left:219px;top:92px">WED</span>
  <span class="cal-cell cal-head" style="left:275px;top:92px">THR</span>
  <span class="cal-cell cal-head" style="left:331px;top:92px">FRI</span>
  <span class="cal-cell cal-head" style="left:392px;top:92px">SAT</span>
  <span class="cal-cell" style="left:275px;top:135px">1</span>
  <span class="cal-cell" style="left:331px;top:135px">2</span>
  <span class="cal-cell" style="left:392px;top:135px">3</span>
  <span class="cal-cell" style="left:43px;top:171px">4</span>
  <span class="cal-cell" style="left:100px;top:171px">5</span>
  <span class="cal-cell" style="left:156px;top:171px">6</span>
  <span class="cal-cell cal-today" style="left:219px;top:171px">7</span>
  <span class="cal-cell" style="left:275px;top:171px">8</span>
  <span class="cal-cell" style="left:331px;top:171px">9</span>
  <span class="cal-cell" style="left:392px;top:171px">10</span>
  <span class="cal-cell" style="left:43px;top:207px">11</span>
  <span class="cal-cell" style="left:100px;top:207px">12</span>
  <span class="cal-cell" style="left:156px;top:207px">13</span>
  <span class="cal-cell" style="left:219px;top:207px">14</span>
  <span class="cal-cell" style="left:275px;top:207px">15</span>
  <span class="cal-cell" style="left:331px;top:207px">16</span>
  <span class="cal-cell" style="left:392px;top:207px">17</span>
  <span class="cal-cell" style="left:43px;top:243px">18</span>
  <span class="cal-cell" style="left:100px;top:243px">19</span>
  <span class="cal-cell" style="left:156px;top:243px">20</span>
  <span class="cal-cell" style="left:219px;top:243px">21</span>
  <span class="cal-cell" style="left:275px;top:243px">22</span>
  <span class="cal-cell" style="left:331px;top:243px">23</span>
  <span class="cal-cell" style="left:392px;top:243px">24</span>
  <span class="cal-cell" style="left:43px;top:279px">25</span>
  <span class="cal-cell" style="left:100px;top:279px">26</span>
  <span class="cal-cell" style="left:156px;top:279px">27</span>
  <span class="cal-cell" style="left:219px;top:279px">28</span>
  <span class="cal-cell" style="left:275px;top:279px">29</span>
  <span class="cal-cell" style="left:331px;top:279px">30</span>
  <span class="cal-cell" style="left:392px;top:279px">31</span>
</div>

<div class="event-img" role="img" aria-label="Red boathouse on a lake" style="top:2082px;background:linear-gradient(135deg,#4f6a3c,#9a3a32 50%,#5d7d8c)"></div>
<div class="event-img" role="img" aria-label="Wooden cottage among trees" style="top:2197px;background:linear-gradient(135deg,#3e5a34,#8a6a4a 55%,#4d6d3a)"></div>
<div class="event-img" role="img" aria-label="Modern cabin lit at night" style="top:2313px;background:linear-gradient(135deg,#1c2024,#7a5330 55%,#2a2d30)"></div>
<div class="event" style="top:2078px"><div class="date">&#9638; 7 June 2023</div><div class="title">Lorem ipsum dolor sit amet.</div><div class="desc">Lorem ipsum dolor sit amet, consectetur adipis cing elit, sed do eiusmod tempor.</div></div>
<div class="event" style="top:2192px"><div class="date">&#9638; 7 June 2023</div><div class="title">Lorem ipsum dolor sit amet.</div><div class="desc">Lorem ipsum dolor sit amet, consectetur adipis cing elit, sed do eiusmod tempor.</div></div>
<div class="event" style="top:2307px"><div class="date">&#9638; 7 June 2023</div><div class="title">Lorem ipsum dolor sit amet.</div><div class="desc">Lorem ipsum dolor sit amet, consectetur adipis cing elit, sed do eiusmod tempor.</div></div>
<div class="btn-outline" style="left:512px;top:2459px;width:174px;height:50px;font-size:18px;font-weight:600;background:rgba(0,0,0,.6)">BOOK NOW</div>

<h2 class="h2 serif" style="top:2732px">Things to Explore near Tarnwood Bay Cottages</h2>
<div class="tile" role="img" aria-label="Visitor centre building at dusk" style="left:128px;top:2829px;background:linear-gradient(180deg,#4a4a6a,#3a2a24 55%,#6a5040)"><span>French River<br>Visitor Centre</span></div>
<div class="tile" role="img" aria-label="Waterfall over rocks in a forest" style="left:453px;top:2829px;background:linear-gradient(180deg,#3d5a2e,#6a7a5a 55%,#8a8a80)"><span>Recollet Falls</span></div>
<div class="tile" role="img" aria-label="Trading post storefront with porch" style="left:778px;top:2829px;background:linear-gradient(180deg,#8a8a88,#5a4030 50%,#5a5a58)"><span>Riverbend<br>Trading Post</span></div>
<div class="tile" role="img" aria-label="Rocky lakeshore with pines" style="left:128px;top:3094px;background:linear-gradient(180deg,#6a6e80,#3a4a3a 50%,#4a5058)"><span>Killarney<br>Provincial Park</span></div>
<div class="tile" role="img" aria-label="Marina dock with boats and canoes" style="left:453px;top:3094px;background:linear-gradient(180deg,#7a8a90,#4a5560 45%,#6a5a50)"><span>Tarnwood Bay<br>Marina</span></div>
<div class="tile" role="img" aria-label="Calm lake at sunset with islands" style="left:778px;top:3094px;background:linear-gradient(180deg,#a8b0b4,#c8b098 45%,#3a4034)"><span>Point Grondine Park</span></div>

<div class="map" role="img" aria-label="Map of the area around Killarney and French River"></div>
<div class="map-pin"></div>

<footer class="footer">
  <div class="footer-brand">Tarnwood Bay Cottages</div>
  <div class="contact" style="left:199px">
    <span class="icon-ring"><svg width="20" height="20" viewBox="0 0 24 24" fill="#fff"><path d="M12 2a7 7 0 0 0-7 7c0 5 7 13 7 13s7-8 7-13a7 7 0 0 0-7-7zm0 9.5A2.5 2.5 0 1 1 12 6.5a2.5 2.5 0 0 1 0 5z"/></svg></span>
    <span>418 Tarnwood Bay Road,<br>Lakeside X0X 0X0</span>
  </div>
  <div class="contact" style="left:518px">
    <span class="icon-ring"><svg width="20" height="20" viewBox="0 0 24 24" fill="#fff"><path d="M6.6 10.8a15.1 15.1 0 0 0 6.6 6.6l2.2-2.2c.3-.3.7-.4 1-.2 1.1.4 2.3.6 3.6.6.6 0 1 .4 1 1V20c0 .6-.4 1-1 1C10.6 21 3 13.4 3 4c0-.6.4-1 1-1h3.5c.6 0 1 .4 1 1 0 1.3.2 2.5.6 3.6.1.3 0 .7-.2 1z"/></svg></span>
    <span>Call Us:<br>+1 555 014 2290</span>
  </div>
  <div class="contact" style="left:750px">
    <span class="icon-ring"><svg width="20" height="20" viewBox="0 0 24 24" fill="#fff"><path d="M3 5h18v14H3z"/><path d="M3 5l9 7 9-7" stroke="#0d0d0d" stroke-width="2" fill="none"/></svg></span>
    <span>Email:<br>support@tarnwoodlets.net</span>
  </div>
  <nav class="footer-nav"><span>Home</span><span>Cottages</span><span>Adventures</span><span>About Us</span><span>Getting Here</span></nav>
  <div class="copyright">&copy; 2023 Tarnwood Bay Cottages. All rights are reserved.</div>
</footer>

</body>
</html>
```